Marigold Premium Business Card Design Project

About the company: Here at Fernhaven Botanics, we focus on cosmetic products that based on essential oils and different kinds of plant essences. All of our raw materials are pure organic and specially selected from local producers in Australia.

I'm here to look for a unique business card design, to replace the current one later on, so I don't have many requirements. Why I wanna restrict designers' creativity?

All I know is: 1. do not make it too complicated, straight forward, simple and pure. 2. this design may be used for other purposes (i.e. logo and slogan on the front, Brand Story and contact details at the back). Therefor, I'd like to have the design for 3 layouts, one only have logo, slogan, contact detials, one for the brand story, the other one for the personal business card with staff's mob etc...

A vector graphic is required, i.e. eps, ai, easy for me to resize.

Round Corner.

Thanks

Plz add "Hand made in Australia" in the design, cheers.

Target Market(s)

Women aged yr 20-50

Industry/Entity Type

Business

Requirements
Must have
• Logo: please see attacment (eps, ai)

Slogan: Moonlit Velvet Glow

Website:www.fernhavenbotanics.com.au

Address: temporary not available

Phone: temporary not available

"Hand made in Australia"

Nice to have
• Prefer round corner

```html
<!DOCTYPE html>
<html lang="en">
<head>
<meta charset="utf-8">
<title>Fernhaven Botanics – Business Card</title>
<link rel="stylesheet" href="https://fonts.googleapis.com/css2?family=EB+Garamond:ital,wght@0,400;0,500;1,400&display=swap">
<style>
  :root {
    --page: #eeeeee;
    --card: #ffffff;
    --crimson: #c2335a;
    --rose: #c94a6c;
    --rose-soft: #e39aac;
    --band-start: #bd2f4f;
    --band-mid: #c9365e;
    --band-end: #dc9196;
    --band-text: #ffffff;
  }
  * { margin: 0; padding: 0; box-sizing: border-box; }
  html, body {
    width: 1200px;
    height: 791px;
    overflow: hidden;
    background: var(--page);
    font-family: "EB Garamond", Garamond, serif;
  }
  .business-card {
    position: absolute;
    left: 41px;
    top: 41px;
    width: 1119px;
    height: 708px;
    background: var(--card);
    border-radius: 38px;
    overflow: hidden;
    box-shadow: 0 2px 12px rgba(0, 0, 0, 0.18);
  }
  .brand-name {
    position: absolute;
    left: 108px;
    top: 150px;
    font-size: 78px;
    font-weight: 400;
    color: var(--crimson);
    line-height: 1;
    white-space: nowrap;
  }
  .brand-dot {
    position: absolute;
    left: 378px;
    top: 257px;
    width: 140px;
    height: 140px;
  }
  .slogan {
    position: absolute;
    left: 109px;
    top: 283px;
    font-size: 22px;
    font-style: italic;
    color: var(--rose);
    white-space: nowrap;
  }
  .contact {
    position: absolute;
    left: 614px;
    top: 420px;
    color: var(--rose);
  }
  .contact__name {
    font-size: 31px;
    font-weight: 400;
    color: var(--crimson);
    line-height: 1.2;
    margin-bottom: 22px;
  }
  .contact__line {
    font-size: 24px;
    line-height: 32px;
    white-space: nowrap;
  }
  .made-in-band {
    position: absolute;
    left: 0;
    bottom: 0;
    width: 100%;
    height: 67px;
    background: linear-gradient(90deg, var(--band-start) 0%, var(--band-mid) 30%, var(--band-end) 100%);
    display: flex;
    align-items: center;
    justify-content: center;
  }
  .made-in-band__text {
    font-size: 21px;
    color: var(--band-text);
  }
</style>
</head>
<body>
  <main class="business-card">
    <h1 class="brand-name">Fernhaven Botanics</h1>
    <svg class="brand-dot" viewBox="0 0 140 140" aria-hidden="true">
      <circle cx="70" cy="70" r="62" fill="var(--rose-soft)"/>
    </svg>
    <p class="slogan">Moonlit Velvet Glow</p>

    <section class="contact">
      <h2 class="contact__name">Name Surname</h2>
      <p class="contact__line">Address: temporary not available</p>
      <p class="contact__line">Phone: temporary not available</p>
      <p class="contact__line">www.fernhavenbotanics.com.au</p>
    </section>

    <footer class="made-in-band">
      <p class="made-in-band__text">“Hand made in Australia”</p>
    </footer>
  </main>
</body>
</html>
```